Media and Film Company Needs a New Website

We produce highly stylized commercials and film pieces for our clients. We also produce live events, both corporate and theatrical. Looking for a site that can show off our client videos - have a polished way to show off our team, and be able to create pages to highlight our clients and give a full overview of our project/process with them. We design simple website for some of our clients - so we are very wordpress familiar, and would like something that doesn't feel like a template.

Target Market(s)

content creators, creative directors, production teams, marketing agencies

Industry/Entity Type

Film Production

Number of Pages Required

4 page

Font styles to use
Sans Serif

Requirements
Must have
• slick looking video embed (from YT or Vimeo)
• project pages - client snapshot (what we did for them, how we did it)
• nice landing page, have our company video reel on the page
• testimonials
• contact page
• ability to have photos as a background if we want
Nice to have
• polished clean look - look to our logo colors and linear elements
• we produce very stylized videos for our clients and our website should reflect that
Should not have
• template look or feel to it- please bring your flare to the project!
• take a look at our current site - brelvostudio.com we need a better way to highlight our work and our clients

```html
<!DOCTYPE html>
<html lang="en">
<head>
<meta charset="utf-8">
<title>Brelvo Media &amp; Entertainment</title>
<link rel="stylesheet" href="https://fonts.googleapis.com/css2?family=Play:wght@400;700&family=Open+Sans:wght@400;600;700&display=swap">
<style>
:root{
  --ink:#222224;
  --dark:#2a2a2c;
  --darker:#1b1b1d;
  --blue:#2a8fd3;
  --magenta:#d81b7d;
  --yellow:#f4c316;
  --cyan:#27a9e1;
  --grey:#8b8b8b;
  --white:#ffffff;
  --muted:#cfcfcf;
}
*{box-sizing:border-box;margin:0;padding:0}
html,body{width:1200px;height:3061px;overflow:hidden}
body{position:relative;font-family:"Open Sans",Arial,sans-serif;color:var(--white);background:var(--darker)}
.band{position:absolute;left:0;width:1200px}
h2{font-family:"Play",Arial,sans-serif;font-weight:700;letter-spacing:1px}

/* top bar */
.topbar{top:0;height:42px;background:var(--dark);display:flex;align-items:center;justify-content:space-between;padding:0 76px}
.social{display:flex;gap:20px}
.social span{width:14px;height:14px;border-radius:50%;background:var(--muted)}
.social span:first-child{background:var(--yellow)}
.callus{display:flex;align-items:center;gap:12px;font-size:16px}
.callus b{font-weight:700}
.callus svg{width:28px;height:28px}

/* nav */
.nav{top:42px;height:84px;background:linear-gradient(#f7f7f7,#e4e4e4);display:flex;align-items:center;padding:0 76px;color:var(--ink)}
.nav ul{list-style:none;display:flex;gap:34px;font-family:"Play",Arial,sans-serif;font-weight:700;font-size:16px}
.nav li.active{border-bottom:3px solid var(--ink);padding-bottom:20px;margin-bottom:-23px}
.brand{flex:1;text-align:center;font-family:"Play",Arial,sans-serif;font-weight:700;font-size:30px;letter-spacing:2px;color:var(--ink)}

/* hero */
.hero{top:126px;height:574px;background:radial-gradient(ellipse at 75% 35%,#3c4a63 0%,#1c2230 55%,#0f121a 100%)}
.hero-photo{position:absolute;left:0;top:0;width:520px;height:574px;background:radial-gradient(ellipse at 45% 45%,#9aa3ad 0%,#4c5561 45%,rgba(20,24,32,0) 80%)}
.hero-title{position:absolute;left:600px;top:104px;width:520px;text-align:center;font-family:"Play",Arial,sans-serif;font-weight:700;line-height:1.05;letter-spacing:2px}
.hero-title .name{display:block;font-size:64px;margin-bottom:26px}
.hero-title .line1{display:block;font-size:76px}
.hero-title .line2{display:block;font-size:46px}

/* welcome */
.welcome{top:700px;height:259px;background:var(--blue);padding:62px 0 0 80px}
.welcome h2{font-size:44px;margin-bottom:22px}
.welcome p{width:600px;font-size:14px;line-height:1.6}

.video-card{position:absolute;left:698px;top:557px;width:424px;height:351px;border:2px solid rgba(255,255,255,.7);background:var(--darker)}
.video-card .shots{position:absolute;inset:0;background:linear-gradient(135deg,#5a5a5a,#1e1e1e 50%,#7a3a1a 85%,#c86a2a)}
.video-card .pitch{position:absolute;left:0;top:31px;width:196px;height:275px;background:var(--magenta);padding:42px 14px 0;font-family:"Play",Arial,sans-serif;font-size:22px;line-height:1.4;text-transform:uppercase}
.play{display:flex;align-items:center;gap:10px;margin-top:30px;font-size:15px}
.play svg{width:18px;height:22px}

/* what we do */
.services{top:959px;height:551px;background:linear-gradient(#262628,#333336);text-align:center;padding-top:50px}
.services h2{font-size:42px}
.services .lead{width:900px;margin:22px auto 0;font-size:15px;line-height:1.6}
.service-row{position:absolute;top:218px;left:78px;width:1060px;display:flex;justify-content:space-between;text-align:left}
.service{width:230px}
.ring{width:124px;height:124px;border-radius:50%;border:6px solid;display:flex;align-items:center;justify-content:center;margin-bottom:16px}
.ring i{width:96px;height:96px;border-radius:50%;display:flex;align-items:center;justify-content:center}
.ring svg{width:48px;height:48px}
.service h3{font-family:"Play",Arial,sans-serif;font-size:23px;line-height:1.05;margin-bottom:10px}
.service ul{list-style:none;font-size:14px;line-height:1.65}
.service li::before{content:"• ";margin-right:4px}

/* about */
.about{top:1510px;height:371px;background:var(--magenta);text-align:center;padding-top:50px}
.about h2{font-size:42px;margin-bottom:20px}
.about p{width:980px;margin:0 auto 26px;font-size:15px;line-height:1.65}
.btn{display:inline-flex;align-items:center;gap:8px;background:var(--white);color:var(--magenta);border-radius:30px;padding:12px 24px;font-size:16px;font-weight:600}

/* portfolio */
.portfolio{top:1881px;height:588px;background:linear-gradient(#1f1f21,#2c2c2e);text-align:center;padding-top:48px}
.portfolio h2{font-size:42px}
.filters{position:relative;margin-top:30px;height:44px;display:flex;justify-content:center;gap:20px}
.filters::before{content:"";position:absolute;left:76px;right:76px;top:22px;border-top:1px solid #8a8a8a}
.filters span{position:relative;border:2px solid var(--yellow);border-radius:24px;padding:8px 26px;font-size:17px;background:var(--darker)}
.filters span.on{background:var(--white);color:var(--ink);border-color:var(--white)}
.grid{position:absolute;top:194px;left:0;display:flex}
.tile{width:400px;height:282px}
.tile.feature{background:var(--yellow);padding-top:80px;position:relative}
.tile.feature::before,.tile.feature::after{content:"";position:absolute;left:0;right:24px;border-top:1px solid rgba(255,255,255,.7)}
.tile.feature::before{top:30px}.tile.feature::after{bottom:30px}
.tile.feature h4{font-family:"Play",Arial,sans-serif;font-size:22px;line-height:1.1;margin-bottom:16px}
.tile.feature .btn{color:var(--yellow);padding:10px 20px;font-size:15px}
.tile.p1{background:linear-gradient(135deg,#b88c5c,#e6ddd2 50%,#7a4c2c)}
.tile.p2{background:linear-gradient(#5d8fb8,#9bbbd6 35%,#7d8a5a 70%,#3d6a2d)}
.view-all{position:absolute;left:0;right:0;top:500px}
.view-all .btn{color:var(--yellow);padding:12px 26px}

/* clients */
.clients{top:2469px;height:157px;background:linear-gradient(90deg,#2a8fd3,#3d9ad8);display:flex;justify-content:center;gap:14px;padding-top:24px}
.clients div{width:163px;height:106px;background:var(--white);display:flex;align-items:center;justify-content:center}
.clients div i{width:90px;height:44px;background:#d4d4d8;border-radius:4px}

/* contact */
.contact{top:2626px;height:175px;background:var(--magenta);display:flex;justify-content:space-between;padding:30px 90px 0 104px;text-align:center;font-size:15px;line-height:1.8}
.contact div{display:flex;flex-direction:column;align-items:center}
.contact .circle{width:64px;height:64px;border:2px solid var(--white);border-radius:50%;display:flex;align-items:center;justify-content:center;margin-bottom:16px}
.contact svg{width:28px;height:28px}

/* form */
.enquiry{top:2801px;height:215px;background:radial-gradient(ellipse at 50% 60%,#3a3632,#141416 70%)}
.field{position:absolute;left:116px;width:333px;height:41px;border:1px solid #cfcfcf;border-radius:4px;font-size:14px;padding:10px 14px;color:#d8d8d8}
.message{left:461px;top:34px;width:624px;height:88px}
.submit{position:absolute;left:461px;top:137px;width:624px;height:41px;background:var(--yellow);border-radius:3px;text-align:center;font-family:"Play",Arial,sans-serif;font-weight:700;font-size:22px;line-height:41px}

.footer{top:3016px;height:45px;background:var(--blue);text-align:center;font-size:14px;line-height:45px}
</style>
</head>
<body>

<header class="band topbar">
  <div class="social"><span></span><span></span><span></span><span></span><span></span></div>
  <div class="callus">Call us now
    <svg viewBox="0 0 28 28" fill="none" stroke="#fff" stroke-width="1.6"><circle cx="14" cy="14" r="12.5"/><path d="M10 8l2.2 3-1.4 1.6c.9 1.8 2.3 3.2 4 4l1.6-1.4 3 2.2-1.2 2.2c-4.6-.4-8.6-4.4-9-9z" fill="#fff" stroke="none"/></svg>
    <b>+1 555 014 2290</b></div>
</header>

<nav class="band nav">
  <ul><li class="active">HOME</li><li>PORTFOLIO</li><li>ABOUT BRELVO</li></ul>
  <div class="brand">BRELVO</div>
  <ul><li>TESTIMONIALS</li><li>PRESS</li><li>CONTACT US</li></ul>
</nav>

<section class="band hero">
  <div class="hero-photo" role="img" aria-label="Vintage film projector in a smoky blue studio"></div>
  <div class="hero-title"><span class="name">BRELVO</span><span class="line1">MEDIA &amp;</span><span class="line2">ENTERTAINMENT</span></div>
</section>

<section class="band welcome">
  <h2>WELCOME TO BRELVO</h2>
  <p>Lorem Ipsum is simply dummy text of the printing and typesetting industry. Lorem Ipsum has been the industry's standard dummy text ever since the 1500s, when an unknown printer took a galley of type and scrambled it to make a type specimen book. It has survived not only five centuries, but also the leap into.</p>
</section>

<div class="video-card">
  <div class="shots" role="img" aria-label="Collage of studio microphone, stage chair and live concert lighting"></div>
  <div class="pitch">The chair is open… how can we help you tell your story?
    <div class="play"><svg viewBox="0 0 18 22"><path d="M0 0l18 11L0 22z" fill="#fff"/></svg>PLAY VIDEO</div>
  </div>
</div>

<section class="band services">
  <h2>WHAT WE DO</h2>
  <p class="lead">Lorem Ipsum is simply dummy text of the printing and typesetting industry. Lorem Ipsum has been the industry's standard dummy text ever since the 1500s, when an unknown printer took a galley of type.</p>
  <div class="service-row">
    <div class="service">
      <div class="ring" style="border-color:var(--grey)"><i style="background:var(--grey)"><svg viewBox="0 0 48 48" fill="#fff"><circle cx="16" cy="14" r="7"/><circle cx="32" cy="14" r="7"/><rect x="8" y="22" width="26" height="16" rx="2"/><path d="M34 27l8-5v16l-8-5z"/></svg></i></div>
      <h3>Film &amp; Media<br>Production</h3>
      <ul><li>Pro Editing Suite</li><li>Motion Graphics</li><li>4k Workflow</li><li>Direct to Web/Streaming</li></ul>
    </div>
    <div class="service">
      <div class="ring" style="border-color:var(--cyan)"><i style="background:var(--blue)"><svg viewBox="0 0 48 48" fill="none" stroke="#fff" stroke-width="3"><circle cx="24" cy="18" r="3" fill="#fff"/><path d="M17 11a10 10 0 000 14M31 11a10 10 0 010 14M12 6a17 17 0 000 24M36 6a17 17 0 010 24M24 22l-8 20M24 22l8 20M19 34h10"/></svg></i></div>
      <h3>Live<br>Production</h3>
      <ul><li>Theatrical Producing</li><li>Production Management</li><li>Lighting &amp; Video Design</li><li>Audio System Design</li></ul>
    </div>
    <div class="service">
      <div class="ring" style="border-color:var(--yellow)"><i style="background:var(--yellow)"><svg viewBox="0 0 48 48" fill="#fff"><path d="M10 30l18-18 8 8-18 18z"/><path d="M8 32l8 8-4 2-6-6z"/><path d="M32 8l2-4M38 14l4-2M36 10l4-4" stroke="#fff" stroke-width="3"/></svg></i></div>
      <h3>PR, Marketing &amp;<br>Advertising</h3>
      <ul><li>Branding</li><li>Social Media</li><li>Media Relations and Outreach</li><li>Street Teams</li></ul>
    </div>
    <div class="service">
      <div class="ring" style="border-color:var(--magenta)"><i style="background:var(--magenta)"><svg viewBox="0 0 48 48" fill="none" stroke="#fff" stroke-width="3"><rect x="8" y="10" width="32" height="30" rx="2"/><path d="M8 18h32M16 6v8M32 6v8"/><path d="M14 24h4M22 24h4M30 24h4M14 31h4M22 31h4M30 31h4" stroke-width="4"/></svg></i></div>
      <h3>Events</h3>
      <ul><li>Event Production</li><li>Staffing &amp; Hiring</li><li>Manage RFPs</li><li>Sponsor Relations</li></ul>
    </div>
  </div>
</section>

<section class="band about">
  <h2>ABOUT BRELVO</h2>
  <p>Brelvo Media &amp; Entertainment provides full-service campaigns in film and media production, live entertainment &amp; theatrical production, marketing &amp; advertising, and event management in the DC metro area.</p>
  <p>Founded in 2009, Brelvo Media &amp; Entertainment has built a reputation working for clients including the Meridian Film Society, Northgate Leaders Forum, Calder Music School, Riverside Community Partners, and Brightline Events.</p>
  <span class="btn">READ MORE <b>»</b></span>
</section>

<section class="band portfolio">
  <h2>OUR PORTFOLIO</h2>
  <div class="filters"><span>ALL</span><span class="on">PHOTOS</span><span>VIDEOS</span></div>
  <div class="grid">
    <div class="tile feature"><h4>Events at the<br>Harlow Center |<br>Kestrel Stage</h4><span class="btn">READ MORE</span></div>
    <div class="tile p1" role="img" aria-label="Community event photos around a partner organisation sign"></div>
    <div class="tile p2" role="img" aria-label="Street view of a shopfront building with flower beds"></div>
  </div>
  <div class="view-all"><span class="btn">VIEW ALL <b>»</b></span></div>
</section>

<section class="band clients">
  <div><i></i></div><div><i></i></div><div><i></i></div><div><i></i></div><div><i></i></div><div><i></i></div>
</section>

<section class="band contact">
  <div><span class="circle"><svg viewBox="0 0 28 28" fill="none" stroke="#fff" stroke-width="2"><path d="M14 26s-8-8.5-8-14a8 8 0 0116 0c0 5.5-8 14-8 14z"/><circle cx="14" cy="12" r="3"/></svg></span>4812 Alder Lane #210<br>Fairmont, MD 20999</div>
  <div><span class="circle"><svg viewBox="0 0 28 28"><path d="M8 4l4 5-2.4 2.6c1.6 3 4 5.4 7 7L19 16l5 4-2 4C13 23 5 15 4 6z" fill="#fff"/></svg></span><b>+1 555 014 2290</b></div>
  <div><span class="circle"><svg viewBox="0 0 28 28" fill="none" stroke="#fff" stroke-width="2"><rect x="4" y="7" width="20" height="14" rx="1"/><path d="M4 8l10 8 10-8"/></svg></span>info@brelvostudio.com</div>
</section>

<section class="band enquiry">
  <div class="field" style="top:34px">Name</div>
  <div class="field" style="top:85px">Phone</div>
  <div class="field" style="top:137px">Email</div>
  <div class="field message">Message</div>
  <div class="submit">SUBMIT</div>
</section>

<footer class="band footer">© <b>BRELVO MEDIA &amp; ENTERTAINMENT</b> - 2017. All Rights Reserved.</footer>

</body>
</html>
```